Business card, postcard, pocket folder

We are a real estate team and have had a new logo designed. From this, we need the following deliverables:- Business Cards (double-sided)- Just Listed / Just Sold Postcards (double-sided)- Pocket Folder. See logo attached.More work possible for the winning designer.
There are 5 members of the team, so head shots should be easily changed and possible for a group photo might be a good idea for the pocket folder but not 100% neccessary.
Target Market(s)
Real estate
Industry/Entity Type
Real Estate
Font styles to use
Serif
Sans Serif
Requirements
Must have
- Business cards and postcards must have a head shot on them.

```html
<!DOCTYPE html>
<html lang="en">
<head>
<meta charset="utf-8">
<title>Harbison Group – Pocket Folder</title>
<link href="https://fonts.googleapis.com/css2?family=Lato:wght@400;700&display=swap" rel="stylesheet">
<style>
:root{
  --stage:#4a5858;
  --blue:#0a1ae8;
  --purple:#5a0fa0;
  --red:#e8030b;
  --paper:#ffffff;
  --paper-shade:#f1f3f3;
  --ink-white:#ffffff;
}
*{box-sizing:border-box;margin:0;padding:0}
html,body{width:904px;height:1200px;overflow:hidden;background:var(--stage)}
body{position:relative;font-family:"Lato",sans-serif}

.folder-inside,.folder-outside{position:absolute;left:46px;width:809px;height:538px;overflow:hidden}
.folder-inside{top:48px;background:var(--paper)}
.folder-outside{top:620px;background:var(--paper)}

.inside-left{position:absolute;left:0;top:0;width:404px;height:100%;
  background:linear-gradient(90deg,var(--paper) 0%,var(--paper-shade) 100%)}
.inside-right{position:absolute;left:404px;top:0;width:405px;height:100%;background:#fbfbfb}
.pockets{position:absolute;left:0;top:360px;width:809px;height:178px}

.back-cover{position:absolute;left:0;top:0;width:404px;height:100%;
  background:linear-gradient(45deg,var(--blue) 0%,var(--purple) 38%,#9a0a55 68%,var(--red) 100%)}
.spine{position:absolute;left:404px;top:0;width:45px;height:100%;
  background:linear-gradient(180deg,var(--red) 0%,#a10a4a 50%,var(--purple) 100%)}
.spine-fold{position:absolute;left:404px;top:0;width:1px;height:100%;background:rgba(255,255,255,.8)}
.front-cover{position:absolute;left:449px;top:0;width:360px;height:100%;background:#fbfbfb}

.brand-name{position:absolute;font-family:"Lato",sans-serif;font-weight:700;letter-spacing:-.5px;white-space:nowrap;transform:translateX(-50%)}
.brand-name--back{left:202px;top:248px;font-size:32px;color:var(--ink-white)}
.brand-name--front{left:181px;top:74px;font-size:28px;color:var(--blue)}
.brand-name--faint{left:181px;top:250px;font-size:62px;color:var(--blue);opacity:.05}

.contact{position:absolute;top:494px;font-size:8.5px;color:var(--ink-white);line-height:14px}
.contact li{list-style:none;display:flex;align-items:center;gap:5px}
.contact svg{width:7px;height:7px;fill:var(--ink-white)}
.contact--phones{left:22px}
.contact--web{left:120px}
.contact--address{left:270px}

.front-url{position:absolute;left:181px;top:500px;transform:translateX(-50%);
  font-size:10px;font-weight:700;letter-spacing:.8px;color:var(--blue);white-space:nowrap}
.front-url-rule{position:absolute;left:163px;top:515px;width:35px;height:1.5px;background:var(--blue)}
</style>
</head>
<body>

<section class="folder-inside" aria-label="Folder inside spread">
  <div class="inside-left"></div>
  <div class="inside-right"></div>
  <svg class="pockets" viewBox="0 0 809 178" width="809" height="178">
    <defs>
      <linearGradient id="pocket-gradient" x1="0" x2="1" y1="0" y2="0">
        <stop offset="0" stop-color="#0a1ae8"/>
        <stop offset=".4" stop-color="#5a0fa0"/>
        <stop offset=".7" stop-color="#a00a4c"/>
        <stop offset="1" stop-color="#e8030b"/>
      </linearGradient>
    </defs>
    <polygon points="0,0 382,0 402,178 0,178" fill="url(#pocket-gradient)"/>
    <polygon points="426,0 809,0 809,178 407,178" fill="url(#pocket-gradient)"/>
    <g class="card-slits" stroke="#fff" stroke-width="0.8">
      <line x1="120" y1="64" x2="142" y2="42"/>
      <line x1="262" y1="42" x2="284" y2="64"/>
      <line x1="120" y1="114" x2="142" y2="136"/>
      <line x1="262" y1="136" x2="284" y2="114"/>
      <line x1="526" y1="64" x2="548" y2="42"/>
      <line x1="667" y1="42" x2="689" y2="64"/>
      <line x1="526" y1="114" x2="548" y2="136"/>
      <line x1="667" y1="136" x2="689" y2="114"/>
    </g>
  </svg>
</section>

<section class="folder-outside" aria-label="Folder outside spread">
  <div class="back-cover">
    <div class="brand-name brand-name--back">Harbison Group</div>
    <ul class="contact contact--phones">
      <li><svg viewBox="0 0 10 10"><path d="M2 0l2 2-1 1.5a6 6 0 0 0 3.5 3.5L8 6l2 2-1.5 2A8 8 0 0 1 0 1.5z"/></svg>555-014-2158</li>
      <li><svg viewBox="0 0 10 10"><rect x="2" y="0" width="6" height="3"/><rect x="0" y="3.5" width="10" height="4"/><rect x="2" y="7" width="6" height="3"/></svg>555-014-9999</li>
    </ul>
    <ul class="contact contact--web">
      <li><svg viewBox="0 0 10 10"><path d="M0 2h10v6H0z M0 2l5 3.5L10 2"/></svg>info@harbisongroup.com</li>
      <li><svg viewBox="0 0 10 10"><circle cx="5" cy="5" r="5"/></svg>www.harbisongroup.com</li>
    </ul>
    <ul class="contact contact--address">
      <li>1180 Alder Street, Lake Haven</li>
      <li>FL 30012</li>
    </ul>
  </div>
  <div class="spine"></div>
  <div class="spine-fold"></div>
  <div class="front-cover">
    <div class="brand-name brand-name--front">Harbison Group</div>
    <div class="brand-name brand-name--faint" aria-hidden="true">Harbison Group</div>
    <div class="front-url">www.harbisongroup.com</div>
    <div class="front-url-rule"></div>
  </div>
</section>

</body>
</html>
```